Powepoint Templates From Logo

We need 3 Powerpoint templates for use in a variety of presentations we develop and customize. Primary uses of the powerpoint presentations are for printed "pitch books" describing our firm's capabilities and approach (a lot of words with some design elements that we have developed), printed presentations of the results of financial evaluations of our clients (lots of charts and graphs) and as the talking points for speeches.

The design needs to be professional and "solid" to establish that we are capable of selling your multi-million dollar business, but also be a little different to show that we are not just boring MBA's.

Our current website and other materials have been developed internally and leave a great deal to be desired. I have initiated this project to demonstrate how much our look can be improved and, if successful, I hope to do much bigger projects in the future.
Updates

This is my first project and I thaank you all for your participation. Since I am new to this, I don;t know if I am providing the help and feedback as I should. Please feel free to let me know how I can be a better customer.

Target Market(s)

professionals (lawyers, accountaants), business owners, business groups, technology people

Industry/Entity Type

Financial

Requirements
Must have
• our logo
a place where logo of client can be inserted if appropriate
templates for the following pages
title page
standard bullet narrative page
page for charts and graphs to mostly fill the page
Should not have a lot of dark solid color that has to be printed.

Nice to have
• something to perk up the color a little

```html
<!DOCTYPE html>
<html lang="en">
<head>
<meta charset="utf-8">
<title>Ledgerline Presentation Templates</title>
<link rel="stylesheet" href="https://fonts.googleapis.com/css2?family=Mulish:wght@300;400;800&family=Arimo:wght@400;700&display=swap">
<style>
  :root {
    --navy: #0d2d63;
    --blue: #2a6cb3;
    --rule: #47689a;
    --slide-grey: #e3e4e6;
    --slide-light: #f7f7f8;
    --card: #ffffff;
    --ink: #1a1a1a;
    --stage: #6b6b6b;
    --green-top: #9ccc8c;
    --green-front-top: #6fae63;
    --green-front-bottom: #9fcf90;
    --green-side: #5f9c52;
  }
  * { margin: 0; padding: 0; box-sizing: border-box; }
  html, body { width: 1200px; height: 849px; overflow: hidden; }
  body { background: var(--stage); position: relative; font-family: "Arimo", Arial, sans-serif; }

  .slide {
    position: absolute; width: 540px; height: 405px; overflow: hidden;
    background: radial-gradient(ellipse at 45% 40%, var(--slide-light) 0%, var(--slide-grey) 75%);
    box-shadow: 0 3px 10px rgba(0,0,0,.45);
  }
  .slide--title { left: 40px; top: 15px; }
  .slide--bullets { left: 620px; top: 15px; }
  .slide--chart { left: 40px; top: 430px; }

  /* Title slide */
  .title-card { position: absolute; left: 28px; top: 22px; width: 484px; height: 363px; background: var(--card); border-radius: 6px; overflow: hidden; }
  .title-card__header { height: 113px; background: var(--navy); position: relative; }
  .title-card__header::after { content: ""; position: absolute; left: 46px; bottom: -8px; border: 8px solid transparent; border-top-color: var(--navy); border-bottom: 0; }
  .brand { position: absolute; left: 78px; top: 56px; font-family: "Mulish", sans-serif; font-weight: 800; font-size: 24px; color: #fff; letter-spacing: .5px; }
  .title-card__title { position: absolute; left: 20px; top: 294px; font-family: "Mulish", sans-serif; font-weight: 800; font-size: 20px; color: var(--navy); white-space: nowrap; }
  .title-card__subtitle { position: absolute; left: 20px; top: 318px; font-family: "Mulish", sans-serif; font-weight: 300; font-size: 13px; color: var(--blue); white-space: nowrap; }

  /* Content slides */
  .slide__topbar { position: absolute; left: 0; top: 0; width: 100%; height: 7px; background: var(--navy); }
  .slide__tab { position: absolute; left: -6px; top: 24px; width: 19px; height: 36px; border-radius: 5px; background: var(--navy); }
  .slide__heading { position: absolute; left: 28px; top: 20px; font-family: "Mulish", sans-serif; font-weight: 800; font-size: 18px; color: var(--navy); }
  .slide__subheading { position: absolute; left: 28px; top: 45px; font-family: "Mulish", sans-serif; font-weight: 300; font-size: 14px; color: var(--blue); }
  .slide__rule { position: absolute; left: 28px; right: 30px; top: 71px; height: 1px; background: var(--rule); }

  .bullet-list { position: absolute; left: 28px; top: 96px; width: 420px; list-style: none; }
  .bullet-list li { position: relative; padding-left: 15px; font-size: 14px; line-height: 20px; color: var(--ink); margin-bottom: 19px; }
  .bullet-list li::before { content: "•"; position: absolute; left: 0; color: var(--blue); font-size: 11px; }

  .footer-brand { position: absolute; right: 30px; bottom: 16px; font-family: "Mulish", sans-serif; font-weight: 800; font-size: 10px; color: var(--navy); }

  .chart { position: absolute; left: 0; top: 0; width: 540px; height: 405px; }
  .chart__value { font-family: "Arimo", sans-serif; font-size: 10px; fill: #222; }
  .chart__year { font-family: "Arimo", sans-serif; font-weight: 700; font-size: 11px; fill: #222; }
</style>
</head>
<body>

<section class="slide slide--title">
  <div class="title-card">
    <header class="title-card__header">
      <div class="brand">LEDGERLINE</div>
    </header>
    <h1 class="title-card__title">Insert The Title of Your Presentation Here</h1>
    <p class="title-card__subtitle">Subtitle of the Presentation or main author’s name here</p>
  </div>
</section>

<section class="slide slide--bullets">
  <div class="slide__topbar"></div>
  <div class="slide__tab"></div>
  <h2 class="slide__heading">Sample Slide - Bullet Points</h2>
  <p class="slide__subheading">Placeholder for subtitle</p>
  <div class="slide__rule"></div>
  <ul class="bullet-list">
    <li>The text demonstrates how your own text will look when you replace the placeholder with your own text.</li>
    <li>The text demonstrates how your own text will look when you replace the placeholder with your own text.</li>
    <li>The text demonstrates how your own text will look when you replace the placeholder with your own text.</li>
  </ul>
  <div class="footer-brand">LEDGERLINE</div>
</section>

<section class="slide slide--chart">
  <div class="slide__topbar"></div>
  <div class="slide__tab"></div>
  <h2 class="slide__heading">Sample Slide - Chart</h2>
  <p class="slide__subheading">Placeholder for subtitle</p>
  <div class="slide__rule"></div>
  <svg class="chart" viewBox="0 0 540 405" aria-label="Area chart of values from 1984 to 2008">
    <defs>
      <linearGradient id="front-fill" x1="0" y1="0" x2="0" y2="1">
        <stop offset="0" stop-color="var(--green-front-top)"/>
        <stop offset="1" stop-color="var(--green-front-bottom)"/>
      </linearGradient>
    </defs>
    <polygon fill="var(--green-top)" points="97,130 118.9,140 140.7,148 162.6,158 184.4,170 206.3,180 228.2,187 250,193 271.9,200 293.7,206 315.6,215 337.5,216 359.3,216 381.2,212 403,205 428,187 406.2,194 384.3,198 362.5,198 340.6,197 318.7,188 296.9,182 275,175 253.2,169 231.3,162 209.4,152 187.6,140 165.7,130 143.9,122 122,112"/>
    <polygon fill="url(#front-fill)" points="97,130 118.9,140 140.7,148 162.6,158 184.4,170 206.3,180 228.2,187 250,193 271.9,200 293.7,206 315.6,215 337.5,216 359.3,216 381.2,212 403,205 403,312 97,282"/>
    <polygon fill="var(--green-side)" points="403,205 428,187 428,290 403,312"/>
    <polyline fill="none" stroke="#fff" stroke-width="2" points="97,130 118.9,140 140.7,148 162.6,158 184.4,170 206.3,180 228.2,187 250,193 271.9,200 293.7,206 315.6,215 337.5,216 359.3,216 381.2,212 403,205"/>
    <g stroke="#ffffff" stroke-opacity=".35" stroke-width=".6">
      <line x1="118.9" y1="140" x2="118.9" y2="284"/><line x1="140.7" y1="148" x2="140.7" y2="286"/>
      <line x1="162.6" y1="158" x2="162.6" y2="288"/><line x1="184.4" y1="170" x2="184.4" y2="291"/>
      <line x1="206.3" y1="180" x2="206.3" y2="293"/><line x1="228.2" y1="187" x2="228.2" y2="295"/>
      <line x1="250" y1="193" x2="250" y2="297"/><line x1="271.9" y1="200" x2="271.9" y2="299"/>
      <line x1="293.7" y1="206" x2="293.7" y2="301"/><line x1="315.6" y1="215" x2="315.6" y2="303"/>
      <line x1="337.5" y1="216" x2="337.5" y2="306"/><line x1="359.3" y1="216" x2="359.3" y2="308"/>
      <line x1="381.2" y1="212" x2="381.2" y2="310"/>
    </g>
    <g class="chart__value" text-anchor="middle">
      <text x="142" y="109">1,95</text><text x="168" y="115">1,85</text><text x="189" y="123">1,77</text>
      <text x="212" y="134">1,67</text><text x="232" y="145">1,55</text><text x="254" y="152">1,45</text>
      <text x="274" y="158">1,38</text><text x="296" y="164">1,32</text><text x="321" y="162">1,25</text>
      <text x="331" y="179">1,19</text><text x="352" y="185">1,10</text><text x="373" y="188">1,09</text>
      <text x="396" y="188">1,09</text><text x="413" y="178">1,13</text><text x="436" y="184">1,20</text>
    </g>
    <g class="chart__year" text-anchor="end">
      <text transform="translate(101,285) rotate(-90)">1984</text>
      <text transform="translate(123,287) rotate(-90)">1995</text>
      <text transform="translate(145,289) rotate(-90)">1996</text>
      <text transform="translate(167,291) rotate(-90)">1997</text>
      <text transform="translate(189,294) rotate(-90)">1998</text>
      <text transform="translate(211,296) rotate(-90)">1999</text>
      <text transform="translate(233,298) rotate(-90)">2000</text>
      <text transform="translate(255,300) rotate(-90)">2001</text>
      <text transform="translate(276,302) rotate(-90)">2002</text>
      <text transform="translate(298,304) rotate(-90)">2003</text>
      <text transform="translate(320,306) rotate(-90)">2004</text>
      <text transform="translate(342,309) rotate(-90)">2005</text>
      <text transform="translate(364,311) rotate(-90)">2006</text>
      <text transform="translate(386,313) rotate(-90)">2007</text>
      <text transform="translate(407,315) rotate(-90)">2008</text>
    </g>
  </svg>
  <div class="footer-brand">LEDGERLINE</div>
</section>

</body>
</html>
```